Design flat ui arx 3 inspired app

Know how you fit in the family and how you relate as a family through a shared Tree.
· Keep track of your family as it expands
· Merge family trees or join a common family Tree
· Share family moments by uploading pictures and videos on your calendar
· Get notifications of all events, additions, and other changes to the family tree
· Know where everyone is by keeping in touch through real-time chats
· Share your Tree with friends on social media
· Search for long lost family members and friends
· A great way for your kids to know where they come from

Providing a mobile app that allows users to not only create their family trees but allow them to invite other family members to participate in the completion of the family tree. • User downloads and installs the mobile app, then they proceed to signing up • Signing up the user should provide the following information; profile picture, first name, last name, date of birth, gender, password, email address, country, current city, mobile number • The next step is verifying the mobile number by asking the user to enter the six digit number that was sent to them via sms • Once the mobile number is verified your next step is to enter your family, start with you parents, then spouse(s) or partner(s), then siblings and children if any. This step should be optional, meaning users can skip this step • The app should have a menu bar at the bottom(action bar) with fiver menu items namely, Home, Edit, Tree, Stats, Calendar. • After the user has been signed in their first experience is the home screen, with the profile picture displayed, along with the user’s first name, last name, and age(all the above should be static). Just below all this are three tabs for notifications, photos, and birthdays. • The notifications tab will list all notifications one after the other in text form, example; Kevin updated his high school, Nora added a new member, Brenda has a graduation party coming up, Gordon updated his work experience, Hilda updated her maiden name, Esther updated her siblings, Milton updated his children etc. • Photo’s tab will list all pictures uploaded sorted by latest pictures uploaded and tagged in. One should be able to scroll through the pictures and then when they click on one they can slide though them one after the next viewing them. One should be able to go back to the home screen by clicking the back button. There should be an option to add more photos and share the current ones. • The last tab should be birthdays, which simply lists all birthdays of people who have been entered into the tree from parents to spouses to siblings to children. The birthdays should be listed sorted by month then day, and you should be able to see how old the person is turning. • The next menu bar is the Edit menu which has three tabs namely personal details, family and advanced details. Personal details will have the profile picture, first name, second name, last name, date of birth, gender, twin(if twin then state), relationship status(list spouse if not single), city or place of birth, and living or not. The next tab is the family tab which list and allows you to edit parents, spouse, siblings, and children. The last tab is advanced details, which is hobbies, languages, education, and work experience. • Then the most important part of the app is the Tree function which displays the users family tree, this is all the people added so far and each person is represented by a square with smooth edges, first name and last name displayed first, then age with a green button showing online and a red one showing offline, and below a profile picture. All the relations showed by a line joining the related people. If the person has many spouses they should be stacked together and kids don’t have to show which parent us theirs. One should be able to edit a profile, view a profile, view stats, invite and share. When you invite that person an sms should be generated and the user can enter the mobile number of the family member and once the family members accepts the invitation they then are a member of the tree who can receive notifications on any changes on the tree. Anyone should be able to invite anyone and everyone should see all notifications from everyone who is a member. • The next menu is the statistics menu which displays gender stats, age distribution, birthdays, relationship status, zodiac signs, living vs not living • The last one is the calendar menu which has a calendar where people can add events, upload media, and when a day is clicked and has events on, they should show at the bottom one after the other.

```html
<!DOCTYPE html>
<html lang="en">
<head>
<meta charset="utf-8">
<title>Kinroot – Welcome, Sign in, Sign up</title>
<link href="https://fonts.googleapis.com/css2?family=Roboto:wght@300;400;500&display=swap" rel="stylesheet">
<style>
  :root{
    --page:#f4f4f6;
    --ink-light:#ffffff;
    --ink-soft:rgba(255,255,255,.85);
    --field:rgba(236,236,238,.86);
    --field-icon:rgba(205,205,210,.9);
    --field-text:#6d6d74;
    --button:#322c44;
    --bar:#3a3148;
    --accent:#8ee04e;
    --toggle:#4cc487;
    --warm-1:#f4a77a;
    --warm-2:#c86a5e;
    --dusk-1:#e8756a;
    --dusk-2:#5a4a6e;
    --dusk-3:#3a3d68;
  }
  *{box-sizing:border-box;margin:0;padding:0}
  html,body{width:1200px;height:675px;overflow:hidden;background:var(--page)}
  body{position:relative;font-family:"Roboto",sans-serif;font-weight:300;color:var(--ink-light)}

  .screen{position:absolute;top:198px;width:269px;height:477px;overflow:hidden}
  .screen--welcome{left:119px}
  .screen--signin{left:479px}
  .screen--signup{left:839px}

  .backdrop{position:absolute;inset:0}
  .backdrop--sunset{background:
      radial-gradient(circle at 62% 18%,rgba(255,236,200,.95) 0,rgba(255,210,160,.6) 22%,transparent 48%),
      linear-gradient(100deg,transparent 70%,rgba(90,60,55,.85) 74%,#5b4038 100%),
      linear-gradient(180deg,var(--warm-1) 0%,var(--warm-2) 45%,#7a5a55 75%,#4e4150 100%)}
  .backdrop--dusk{background:
      radial-gradient(circle at 20% 8%,rgba(240,110,110,.9) 0,transparent 40%),
      radial-gradient(circle at 85% 20%,rgba(235,170,120,.7) 0,transparent 40%),
      linear-gradient(180deg,var(--dusk-1) 0%,#b9606a 22%,var(--dusk-2) 50%,var(--dusk-3) 100%)}

  .status{position:absolute;top:5px;left:6px;right:6px;height:14px;font-size:10px;font-weight:400;display:flex;align-items:center;justify-content:space-between}
  .status__left,.status__right{display:flex;align-items:center;gap:4px}
  .status__time{position:absolute;left:50%;transform:translateX(-50%)}

  .center{position:absolute;left:0;right:0;text-align:center}

  /* welcome */
  .brand-mark{position:absolute;left:95px;top:136px;width:88px;height:88px;border-radius:50%;background:#2f2a3d}
  .wordmark{top:232px;font-size:33px;font-weight:300;letter-spacing:3px}
  .tagline-small{position:absolute;left:11px;top:376px;font-size:9.5px;font-weight:400}
  .tagline-large{position:absolute;left:11px;top:390px;font-size:19px;font-weight:300}
  .action-bar{position:absolute;left:0;right:0;top:425px;bottom:0;background:rgba(52,44,66,.92);display:flex;align-items:center}
  .action-bar__item{flex:1;text-align:center;font-size:14px;font-weight:300;padding-bottom:2px}
  .action-bar__divider{width:2px;height:32px;background:var(--accent)}

  /* sign in */
  .mini-brand{top:48px;display:flex;justify-content:center;align-items:center;gap:6px;font-size:15px;font-weight:400;letter-spacing:1px}
  .mini-brand__dot{width:12px;height:12px;border-radius:50%;background:var(--accent)}
  .welcome{font-size:12.5px;font-weight:400}
  .heading{font-size:17.5px;font-weight:300}

  .field{position:absolute;height:29px;background:var(--field);display:flex;align-items:center;font-size:9.5px;font-weight:400;color:var(--field-text)}
  .field__icon{width:31px;height:100%;background:var(--field-icon);display:flex;align-items:center;justify-content:center}
  .field__label{padding-left:11px}
  .field--toggle{background:var(--field);justify-content:stretch}
  .toggle__on{width:115px;height:100%;background:var(--toggle);color:#fff;display:flex;align-items:center;justify-content:center}
  .toggle__off{flex:1;display:flex;align-items:center;justify-content:center;color:#b4b4b8}
  .field__trail{margin-left:auto;width:28px;height:100%;display:flex;align-items:center;justify-content:center}

  .remember{position:absolute;right:21px;top:291px;font-size:9.5px;font-weight:400;display:flex;align-items:center;gap:5px}
  .remember__box{width:9px;height:9px;border:1px solid #fff;border-radius:2px}

  .button{position:absolute;left:45px;width:177px;height:31px;background:var(--button);display:flex;align-items:center;justify-content:center;font-size:14px;font-weight:400}
  .link-small{font-size:9.5px;font-weight:400}
  .link-bold{font-size:10px;font-weight:500}
  .link-bold u{font-weight:500}

  .avatar{position:absolute;left:101px;top:72px;width:64px;height:64px;border-radius:50%;border:2px solid var(--toggle);background:#fff;overflow:hidden}
</style>
</head>
<body>

<!-- Welcome screen -->
<section class="screen screen--welcome">
  <div class="backdrop backdrop--sunset" role="img" aria-label="Warm sunset photo with soft bokeh light beside a tree trunk"></div>
  <div class="status">
    <span class="status__left">●●●○○ NOVA
      <svg width="10" height="8" viewBox="0 0 10 8"><path d="M5 7.5 1 3a6 6 0 0 1 8 0z" fill="#fff"/></svg></span>
    <span class="status__time">4:21 PM</span>
    <span class="status__right">100%
      <svg width="20" height="9" viewBox="0 0 20 9"><rect x=".5" y=".5" width="17" height="8" rx="1.5" fill="none" stroke="#fff"/><rect x="2" y="2" width="14" height="5" fill="#fff"/><rect x="18.5" y="3" width="1.5" height="3" fill="#fff"/></svg></span>
  </div>
  <div class="brand-mark"></div>
  <div class="center wordmark">kinroot</div>
  <p class="tagline-small">Know how you fit in the family and how you relate as a family</p>
  <p class="tagline-large">Through a shared Tree.</p>
  <nav class="action-bar">
    <span class="action-bar__item">Login</span>
    <span class="action-bar__divider"></span>
    <span class="action-bar__item">Sign up</span>
  </nav>
</section>

<!-- Sign in screen -->
<section class="screen screen--signin">
  <div class="backdrop backdrop--dusk" role="img" aria-label="Blurred dusk photo in coral, rose and indigo tones"></div>
  <div class="status">
    <span class="status__left">●●●○○ NOVA
      <svg width="10" height="8" viewBox="0 0 10 8"><path d="M5 7.5 1 3a6 6 0 0 1 8 0z" fill="#fff"/></svg></span>
    <span class="status__time">4:21 PM</span>
    <span class="status__right">
      <svg width="6" height="10" viewBox="0 0 6 10"><path d="M1 2.5 5 7 3 9V1l2 2-4 4.5" fill="none" stroke="#fff" stroke-width="1"/></svg>100%
      <svg width="20" height="9" viewBox="0 0 20 9"><rect x=".5" y=".5" width="17" height="8" rx="1.5" fill="none" stroke="#fff"/><rect x="2" y="2" width="14" height="5" fill="#fff"/><rect x="18.5" y="3" width="1.5" height="3" fill="#fff"/></svg></span>
  </div>
  <div class="center mini-brand"><span class="mini-brand__dot"></span>kinroot</div>
  <p class="center welcome" style="top:110px">Welcome Back to KINROOT</p>
  <p class="center heading" style="top:180px">Sign in here</p>

  <div class="field" style="left:20px;top:209px;width:230px">
    <span class="field__icon"><svg width="11" height="11" viewBox="0 0 11 11"><circle cx="5.5" cy="3" r="2.6" fill="#3a3445"/><path d="M0.5 11a5 4.5 0 0 1 10 0z" fill="#3a3445"/></svg></span>
    <span class="field__label">mobile number</span>
  </div>
  <div class="field" style="left:20px;top:248px;width:230px">
    <span class="field__icon"><svg width="16" height="8" viewBox="0 0 16 8"><circle cx="4" cy="4" r="3" fill="none" stroke="#3a3445" stroke-width="2"/><path d="M7 4h8M12 4v3M14.5 4v2.5" stroke="#3a3445" stroke-width="1.8"/></svg></span>
    <span class="field__label">password</span>
  </div>
  <div class="remember"><span class="remember__box"></span>Remember Me</div>
  <div class="button" style="top:316px">sign in</div>
  <p class="center link-small" style="top:402px">Forget Password ?</p>
  <p class="center link-bold" style="top:453px">New user Sign up</p>
</section>

<!-- Sign up screen -->
<section class="screen screen--signup">
  <div class="backdrop backdrop--dusk" role="img" aria-label="Blurred dusk photo in coral, rose and indigo tones"></div>
  <p class="center welcome" style="top:14px">Welcome Back to KINROOT</p>
  <p class="center heading" style="top:32px">Sign up Here</p>
  <div class="avatar">
    <svg width="60" height="60" viewBox="0 0 60 60"><rect width="60" height="60" fill="#fff"/><circle cx="30" cy="23" r="11" fill="#c7c7cb"/><path d="M8 58a22 20 0 0 1 44 0z" fill="#c7c7cb"/></svg>
  </div>

  <div class="field" style="left:22px;top:154px;width:231px">
    <span class="field__icon"><svg width="16" height="11" viewBox="0 0 16 11"><rect width="16" height="11" fill="#c9485b"/><rect y="2" width="16" height="1.5" fill="#fff"/><rect y="5" width="16" height="1.5" fill="#fff"/><rect y="8" width="16" height="1.5" fill="#fff"/><rect width="7" height="6" fill="#3c4a8a"/></svg></span>
    <span class="field__label">mobile number</span>
  </div>
  <div class="field" style="left:22px;top:191px;width:231px"><span class="field__label">password</span></div>
  <div class="field" style="left:22px;top:228px;width:231px"><span class="field__label">confirm password</span></div>
  <div class="field" style="left:22px;top:265px;width:121px"><span class="field__label">first name</span></div>
  <div class="field" style="left:150px;top:265px;width:103px"><span class="field__label">last Name</span></div>
  <div class="field field--toggle" style="left:22px;top:306px;width:231px">
    <span class="toggle__on">Male</span><span class="toggle__off">Female</span>
  </div>
  <div class="field" style="left:22px;top:345px;width:231px">
    <span class="field__label">current city</span>
    <span class="field__trail"><svg width="14" height="14" viewBox="0 0 14 14"><circle cx="7" cy="7" r="4.2" fill="none" stroke="#bdbdc2"/><circle cx="7" cy="7" r="1.8" fill="#bdbdc2"/><path d="M7 0v2.5M7 11.5V14M0 7h2.5M11.5 7H14" stroke="#bdbdc2"/></svg></span>
  </div>
  <div class="button" style="top:392px;left:44px">Next</div>
  <p class="center link-small" style="top:451px;font-size:10.5px">Existing user <span class="link-bold"><u>Sing in</u></span></p>
</section>

</body>
</html>
```